Funeral Custom Banner
Banner
Project: Funeral Custom Banner
Industry: Funerals Logo
Funeral Custom Banner  - Funerals
Creative Brief
On Lâm Hoàng
Below are details need to be included in the banners. Please use upload photo for this funeral banner On Lam Hoang 1942 - 2023 Rest In Peace You are always on our minds And forever in our hearts! Please use cross sign (catholic logo) for this banner and border as well After the winner is selected, please duplicate the exact banner into 4 banners with different dates as follows: 1942-2023 Rest In Peace 1942-2024 Rest In Peace 1942-2025 Rest In Peace 1942-2026 Rest In Peace Thank you!
Unique/Creative
Black and White and Orange

```html
<!DOCTYPE html>
<html lang="vi">
<head>
<meta charset="utf-8">
<title>On Lâm Hoàng – Memorial Banners</title>
<link rel="stylesheet" href="https://fonts.googleapis.com/css2?family=Alegreya+Sans:wght@400;500&family=Marcellus+SC&family=Arimo:wght@700&display=swap">
<style>
:root{
  --stage:#8b8b8b;
  --paper:#ffffff;
  --paper-tint:#f3f3f3;
  --ink:#1b1b1b;
  --frame:#3f3f3f;
  --accent:#ea6a1f;
  --photo-a:#c4c4c4;
  --photo-b:#5f6770;
  --bloom:#e4e4e4;
  --scroll:#bdbdbd;
}
*{box-sizing:border-box;margin:0;padding:0}
html,body{width:1200px;height:871px;overflow:hidden}
body{background:var(--stage);position:relative;font-family:"Alegreya Sans",sans-serif;color:var(--ink)}
.banner{position:absolute;background:radial-gradient(circle at 50% 40%,var(--paper) 0%,var(--paper) 55%,var(--paper-tint) 100%);overflow:hidden}
.banner--tall{left:108px;top:60px;width:212px;height:660px}
.banner--square{left:338px;top:60px;width:754px;height:619px}
.banner--strip{left:338px;top:696px;width:754px;height:108px}
.abs{position:absolute}
.center-x{left:50%;transform:translateX(-50%)}
.portrait{position:absolute}
.portrait__photo{position:absolute;inset:0;background:linear-gradient(180deg,var(--photo-a) 0%,#959ca3 55%,var(--photo-b) 100%);
  clip-path:polygon(4% 100%,4% 21%,15% 21%,15% 10%,30% 10%,30% 3%,70% 3%,70% 10%,85% 10%,85% 21%,96% 21%,96% 100%)}
.portrait svg{position:absolute;inset:0;width:100%;height:100%;overflow:visible}
.bloom{position:absolute;background:radial-gradient(ellipse closest-side,rgba(255,255,255,.95) 0%,rgba(240,240,240,.9) 45%,rgba(228,228,228,.55) 75%,rgba(228,228,228,0) 100%)}
.flourish{position:absolute;height:6px;background:radial-gradient(ellipse closest-side,#7a7a7a 0%,rgba(122,122,122,.5) 60%,rgba(122,122,122,0) 100%)}
.scroll-ornament{position:absolute;width:46px;height:26px;background:radial-gradient(ellipse closest-side,rgba(170,170,170,.55) 0%,rgba(190,190,190,.3) 60%,rgba(190,190,190,0) 100%)}
.name{position:absolute;white-space:nowrap;color:var(--accent);font-weight:500;line-height:1}
.years{position:absolute;white-space:nowrap;font-weight:400;line-height:1}
.rip{position:absolute;white-space:nowrap;font-family:"Marcellus SC",serif;text-align:center;line-height:1}
.tagline{position:absolute;font-family:"Arimo",sans-serif;font-weight:700;text-align:center}
</style>
</head>
<body>

<section class="banner banner--tall">
  <div class="scroll-ornament" style="left:6px;top:8px" role="img" aria-label="Scroll corner ornament"></div>
  <div class="scroll-ornament" style="right:6px;top:8px" role="img" aria-label="Scroll corner ornament"></div>
  <div class="portrait" style="left:46px;top:78px;width:120px;height:130px">
    <div class="portrait__photo" role="img" aria-label="Portrait photograph of On Lâm Hoàng"></div>
    <svg viewBox="0 0 100 100" preserveAspectRatio="none"><path d="M4 100V21H15V10H30V3H70V10H85V21H96V100" fill="none" stroke="var(--frame)" stroke-width="1.6" vector-effect="non-scaling-stroke"/></svg>
  </div>
  <div class="bloom" style="left:50px;top:186px;width:124px;height:44px" role="img" aria-label="White flower arrangement"></div>
  <svg class="abs" style="left:98px;top:262px" width="16" height="26" viewBox="0 0 16 26"><path d="M6 0h4v7h6v4h-6v15h-4V11H0V7h6z" fill="var(--ink)"/></svg>
  <div class="flourish" style="left:56px;top:290px;width:100px"></div>
  <div class="name center-x" style="top:310px;font-size:24px">On Lâm Hoàng</div>
  <div class="years center-x" style="top:390px;font-size:26px">1942 - 2023</div>
  <div class="rip center-x" style="top:438px;font-size:36px;letter-spacing:3px">Rest</div>
  <div class="rip center-x" style="top:480px;font-size:22px;letter-spacing:2px">In</div>
  <div class="rip center-x" style="top:510px;font-size:36px;letter-spacing:3px">Peace</div>
  <p class="tagline center-x" style="top:606px;width:160px;font-size:14px;line-height:17px">You are always on our minds and forever in our hearts!</p>
</section>

<section class="banner banner--square">
  <div class="portrait" style="left:266px;top:40px;width:226px;height:224px">
    <div class="portrait__photo" role="img" aria-label="Portrait photograph of On Lâm Hoàng"></div>
    <svg viewBox="0 0 100 100" preserveAspectRatio="none"><path d="M4 100V21H15V10H30V3H70V10H85V21H96V100" fill="none" stroke="var(--frame)" stroke-width="2.4" vector-effect="non-scaling-stroke"/></svg>
  </div>
  <div class="bloom" style="left:254px;top:222px;width:250px;height:100px" role="img" aria-label="White flower arrangement"></div>
  <svg class="abs" style="left:367px;top:320px" width="20" height="32" viewBox="0 0 16 26"><path d="M6 0h4v7h6v4h-6v15h-4V11H0V7h6z" fill="var(--ink)"/></svg>
  <div class="flourish" style="left:297px;top:354px;width:160px;height:8px"></div>
  <div class="name center-x" style="top:396px;font-size:48px">On Lâm Hoàng</div>
  <div class="years center-x" style="top:466px;font-size:32px">1942 - 2023</div>
  <div class="rip center-x" style="top:518px;font-size:42px;letter-spacing:7px">Rest In Peace</div>
  <p class="tagline center-x" style="top:564px;width:700px;font-size:20px;white-space:nowrap">You are always on our minds and forever in our hearts!</p>
</section>

<section class="banner banner--strip">
  <div class="scroll-ornament" style="left:8px;top:8px" role="img" aria-label="Scroll corner ornament"></div>
  <div class="scroll-ornament" style="right:8px;top:8px" role="img" aria-label="Scroll corner ornament"></div>
  <div class="portrait" style="left:142px;top:16px;width:56px;height:68px">
    <div class="portrait__photo" role="img" aria-label="Portrait photograph of On Lâm Hoàng"></div>
    <svg viewBox="0 0 100 100" preserveAspectRatio="none"><path d="M4 100V21H15V10H30V3H70V10H85V21H96V100" fill="none" stroke="var(--frame)" stroke-width="1.4" vector-effect="non-scaling-stroke"/></svg>
  </div>
  <div class="name" style="left:228px;top:40px;font-size:24px">On Lâm Hoàng</div>
  <svg class="abs" style="left:528px;top:12px" width="12" height="19" viewBox="0 0 16 26"><path d="M6 0h4v7h6v4h-6v15h-4V11H0V7h6z" fill="var(--ink)"/></svg>
  <div class="flourish" style="left:494px;top:32px;width:80px;height:5px"></div>
</section>

</body>
</html>
```